New business Cards

We need some new cards that stand out. We love our logo and colour scheme but need to incorporate a numo logo and ptl logo yet still keep our cards uncluttered and clean looking.
Our tag is Keen Ledgerworks. Anywhere, Anytime.
The idea of the cards is to show authority in accounting and Numo/ cloud software

```html
<!DOCTYPE html>
<html lang="en">
<head>
<meta charset="utf-8">
<title>Marlow Business Solutions – Business Cards</title>
<link href="https://fonts.googleapis.com/css2?family=Open+Sans:wght@400;600;700&family=Arimo:wght@400;700&family=Uncial+Antiqua&display=swap" rel="stylesheet">
<style>
  :root {
    --bg: #e9eaea;
    --green: #6cbf45;
    --green-dark: #4e9a2c;
    --ink: #1b1b1b;
    --band: #262425;
    --white: #ffffff;
    --teal: #1fa6c4;
    --teal-deep: #17879e;
    --badge-blue: #1d5fa8;
    --badge-gold: #f5c11c;
  }
  * { box-sizing: border-box; margin: 0; padding: 0; }
  html, body { width: 1200px; height: 900px; overflow: hidden; }
  body {
    background: var(--bg);
    display: flex;
    align-items: center;
    justify-content: center;
    gap: 40px;
    font-family: "Open Sans", sans-serif;
  }
  .card {
    position: relative;
    width: 550px;
    height: 335px;
    overflow: hidden;
    box-shadow: 0 6px 18px rgba(0,0,0,.18);
  }

  /* Front */
  .card-front { background: var(--green); }
  .front-brand {
    position: absolute;
    left: 50px; top: 92px;
    display: flex; align-items: center; gap: 22px;
  }
  .brand-square {
    width: 108px; height: 108px;
    background: var(--white);
  }
  .brand-name {
    color: var(--white);
    font-weight: 600;
    font-size: 33px;
    line-height: 1.08;
    letter-spacing: -0.3px;
  }
  .front-band {
    position: absolute;
    left: 0; right: 0; bottom: 0;
    height: 78px;
    background: var(--band);
    display: flex; align-items: center; justify-content: center;
    padding: 0 24px;
  }
  .tagline {
    color: var(--white);
    font-family: "Uncial Antiqua", serif;
    font-size: 19px;
    white-space: nowrap;
    letter-spacing: 0.2px;
  }

  /* Back */
  .card-back { background: var(--white); }
  .back-brand {
    position: absolute;
    right: 26px; top: 20px;
    display: flex; align-items: center; gap: 10px;
  }
  .back-brand .brand-square {
    width: 52px; height: 52px;
    background: var(--green);
  }
  .back-brand .brand-name {
    color: var(--green-dark);
    font-size: 15px;
  }
  .rule {
    position: absolute;
    left: 0; right: 0;
    height: 3px;
    background: var(--green);
  }
  .rule-top { top: 92px; }
  .rule-mid { top: 102px; height: 2px; }
  .name-band {
    position: absolute;
    left: 22px; top: 114px;
    width: 330px; height: 54px;
    background: var(--green);
    padding: 4px 12px;
  }
  .person-name {
    font-family: "Arimo", sans-serif;
    font-weight: 700;
    font-size: 24px;
    color: var(--ink);
    line-height: 1.05;
    white-space: nowrap;
  }
  .credentials {
    font-weight: 400;
    font-size: 12px;
    letter-spacing: .5px;
  }
  .person-role {
    font-family: "Arimo", sans-serif;
    font-weight: 700;
    font-size: 15px;
    color: var(--white);
  }
  .contact {
    position: absolute;
    left: 40px; top: 182px;
    font-family: "Arimo", sans-serif;
    font-weight: 700;
    font-size: 15.5px;
    color: var(--ink);
    line-height: 1.55;
    letter-spacing: .6px;
    list-style: none;
    white-space: nowrap;
  }
  .contact .label { display: inline-block; width: 22px; }
  .badges {
    position: absolute;
    right: 22px; top: 124px;
    display: flex; align-items: center; gap: 6px;
  }
  .badge-round { width: 28px; height: 28px; border-radius: 50%; }
  .badge-numo { background: var(--teal); }
  .badge-advisor { background: var(--teal-deep); }
  .badge-ptl {
    width: 76px; height: 28px;
    background: var(--badge-blue);
    border-right: 18px solid var(--badge-gold);
  }
</style>
</head>
<body>

  <section class="card card-front" aria-label="Business card front">
    <div class="front-brand">
      <div class="brand-square"></div>
      <div class="brand-name">Marlow<br>Business Solutions</div>
    </div>
    <div class="front-band">
      <p class="tagline">Keen Ledgerworks. Anywhere, Anytime.</p>
    </div>
  </section>

  <section class="card card-back" aria-label="Business card back">
    <div class="back-brand">
      <div class="brand-name">Marlow Business Solutions</div>
      <div class="brand-square"></div>
    </div>
    <div class="rule rule-top"></div>
    <div class="rule rule-mid"></div>
    <div class="name-band">
      <p class="person-name">Ellen Marlow<span class="credentials">, PTL, CTA</span></p>
      <p class="person-role">Partner</p>
    </div>
    <div class="badges" aria-label="Partner and membership badges">
      <div class="badge-round badge-numo"></div>
      <div class="badge-round badge-advisor"></div>
      <div class="badge-ptl"></div>
    </div>
    <ul class="contact">
      <li>Kinross Vic 3580</li>
      <li><span class="label">p:</span>03 5550 1824</li>
      <li><span class="label">e:</span>ellenm@marlowbizsol.com.au</li>
      <li>www.marlowbizsol.com.au</li>
    </ul>
  </section>

</body>
</html>
```